Tallow HVAC Services - High end letter head, Quote Template & Invoice Template

Provide word documents for the below.
- Letterhead for emails & letters.
- Quote template (similar to the attached)
- Invoice template (similar to the attached)
Logo colours should be used.
Modern, bold, professional look.
Tallow Logo - Veskor Specialist Dealer logo - Contact information

See attachments of previously used documents.

Target Market(s)

High end clients

Industry/Entity Type

Air Conditioning & Mechanical Ventilation (HVAC)

Font styles to use
Sans Serif
Other font styles liked:
• Arial Narrow or similar - Text similar to the TALLOW logo

Requirements
Must have
• Tallow Logo - Veskor Specialist Dealer logo - Contact information
Nice to have
• Logo colours used throughout the documents
Should not have
• Bright colours, yellow, pink, green etc

```html
<!DOCTYPE html>
<html lang="en">
<head>
<meta charset="utf-8">
<title>Tallow HVAC Services – Stationery</title>
<link rel="stylesheet" href="https://fonts.googleapis.com/css2?family=Montserrat:wght@400;500;600;700;800&family=Roboto:wght@400;500;700&family=Roboto+Condensed:wght@400;700&display=swap">
<style>
:root{
  --backdrop:#e6e7e9;
  --paper:#ffffff;
  --brand-blue:#0b6fba;
  --brand-red:#c8102e;
  --ink:#3a3a3a;
  --ink-soft:#555;
  --rule:#8a8a8a;
  --sig-fill:#eceef1;
}
*{margin:0;padding:0;box-sizing:border-box}
html,body{width:1200px;height:626px;overflow:hidden;background:var(--backdrop)}
body{position:relative;font-family:"Roboto",Arial,sans-serif;color:var(--ink)}
.page{position:absolute;top:84px;width:323px;height:457px;background:var(--paper)}
.page--letterhead{left:60px}
.page--invoice{left:440px}
.page--quote{left:820px}
.abs{position:absolute;white-space:nowrap}

.brand{position:absolute;left:14px;top:10px;display:flex;align-items:center;gap:5px;color:var(--brand-blue);font-family:"Roboto Condensed",Arial,sans-serif;font-weight:700}
.brand__dot{width:18px;height:18px;border-radius:50%;background:var(--brand-blue)}
.brand__name{font-size:17px;line-height:15px;letter-spacing:.5px}
.brand__sub{font-size:6px;line-height:7px;letter-spacing:.3px}

.contact{position:absolute;font-family:"Roboto Condensed",Arial,sans-serif;font-size:6px;line-height:7.6px;color:var(--ink)}
.contact li{list-style:none;display:flex;align-items:center;gap:3px}
.ico{width:5px;height:5px;flex:none}

.signoff{position:absolute;left:12px;font-family:"Montserrat",Arial,sans-serif;color:var(--brand-blue);font-size:5.6px;line-height:7.2px;letter-spacing:.4px}
.signoff__name{font-weight:800;font-size:6px}
.signoff li{list-style:none;display:flex;align-items:center;gap:3px}
.signoff--compact{font-size:4.6px;line-height:6px}
.signoff--compact .signoff__name{font-size:5.2px}

/* invoice */
.doc-title{left:26px;top:55px;font-family:"Montserrat",Arial,sans-serif;font-weight:800;font-size:11.5px;color:var(--brand-blue);letter-spacing:.6px}
.meta{font-family:"Montserrat",Arial,sans-serif;font-weight:700;color:#555;font-size:7px}
.meta__value{font-size:5.8px;letter-spacing:.4px}
.items{position:absolute;left:27px;top:115px;width:270px;border-collapse:collapse;font-family:"Montserrat",Arial,sans-serif;font-size:5.7px;letter-spacing:.35px;color:var(--ink)}
.items th{height:18px;border-top:1.2px solid var(--brand-blue);border-bottom:1.2px solid var(--brand-blue);color:var(--brand-blue);font-weight:600;text-align:left}
.items th:first-child{border-left:1.2px solid var(--brand-blue);padding-left:7px}
.items th:last-child{border-right:1.2px solid var(--brand-blue)}
.items td{height:26.8px;border-bottom:.7px solid var(--rule)}
.items td:first-child{padding-left:9px}
.items tr.blank td{height:26.5px}
.c-sl{width:23px}.c-desc{width:127px}.c-price{width:46px}.c-qty{width:37px}
.pay-note{left:27px;top:285px;color:var(--brand-red);font-weight:700;font-size:6px;line-height:7px}
.sum{font-family:"Montserrat",Arial,sans-serif;font-weight:700;font-size:6px;letter-spacing:.4px;color:#444}
.sum-rule{position:absolute;left:208px;top:309px;width:89px;border-top:.7px solid var(--rule)}
.sum--total{font-size:8.2px}
.sum--total-value{color:var(--brand-blue)}
.due{color:var(--brand-blue);font-weight:700;font-size:5.8px}
.bank{left:27px;top:338px;font-size:6px;line-height:7.3px;color:#333}
.bank dt{float:left;clear:left;width:37px}
.bank dd{margin-left:37px}

/* quote */
.fields{left:18px;top:83px;font-weight:700;font-size:5.8px;line-height:9.3px;color:#333}
.fields .plain{font-weight:400}
.quote-ref{left:231px;top:82px;font-weight:500;font-size:7.6px;line-height:10px;color:#333}
.validity{left:214px;top:115px;font-weight:700;font-size:11px;color:var(--brand-blue)}
.proposal{left:18px;top:165px;font-size:5.8px;color:#444}
.proposal-line{position:absolute;left:161px;top:171px;width:139px;border-top:.6px solid #444}
.body-copy{position:absolute;left:18px;top:179px;width:270px;font-size:5.8px;line-height:7.4px;color:#444}
.description{left:18px;top:208px;font-size:5.8px;color:#444}
.quote-total{left:0;width:323px;top:237px;text-align:center;font-weight:700;font-size:10.6px;color:var(--brand-blue)}
.regards{right:29px;top:300px;font-size:7.6px;color:#444}
.signature{position:absolute;left:229px;top:316px;width:79px;height:24px;background:var(--sig-fill);border-radius:3px}
</style>
</head>
<body>
<svg width="0" height="0" style="position:absolute" aria-hidden="true">
  <symbol id="i-phone" viewBox="0 0 10 10"><path d="M2 1h2l1 2.5-1.3 1a6 6 0 0 0 2.8 2.8l1-1.3L10 7v2c0 .5-.5 1-1 1A9 9 0 0 1 0 1c0-.5.5-1 1-1z" fill="#0b6fba"/></symbol>
  <symbol id="i-mail" viewBox="0 0 10 10"><rect x="0" y="2" width="10" height="6.5" fill="#0b6fba"/><path d="M0 2l5 3.5L10 2" stroke="#fff" stroke-width="1" fill="none"/></symbol>
  <symbol id="i-web" viewBox="0 0 10 10"><circle cx="5" cy="5" r="4.5" fill="#0b6fba"/><path d="M.5 5h9M5 .5c-2.5 3-2.5 6 0 9M5 .5c2.5 3 2.5 6 0 9" stroke="#fff" stroke-width=".7" fill="none"/></symbol>
  <symbol id="i-pin" viewBox="0 0 10 10"><path d="M5 0a3.5 3.5 0 0 1 3.5 3.5C8.5 6 5 10 5 10S1.5 6 1.5 3.5A3.5 3.5 0 0 1 5 0z" fill="#0b6fba"/><circle cx="5" cy="3.5" r="1.3" fill="#fff"/></symbol>
  <symbol id="i-doc" viewBox="0 0 10 10"><rect x="1.5" y="0.5" width="7" height="9" fill="#0b6fba"/><path d="M3 3h4M3 5h4M3 7h3" stroke="#fff" stroke-width=".8"/></symbol>
</svg>

<!-- Letterhead -->
<section class="page page--letterhead" aria-label="Letterhead">
  <div class="brand"><span class="brand__dot"></span><div><div class="brand__name">TALLOW</div><div class="brand__sub">HVAC SERVICES PTY LTD.</div></div></div>
  <ul class="contact" style="left:14px;top:35px">
    <li><svg class="ico"><use href="#i-phone"/></svg>0400 123 456</li>
    <li><svg class="ico"><use href="#i-mail"/></svg>rod@tallowhvac.example</li>
    <li><svg class="ico"><use href="#i-web"/></svg>www.tallowhvac.example</li>
  </ul>
  <ul class="signoff" style="top:408px">
    <li class="signoff__name" style="padding-left:8px">ROD TALLOW</li>
    <li><svg class="ico"><use href="#i-phone"/></svg>0400 123 456</li>
    <li><svg class="ico"><use href="#i-mail"/></svg>rod@tallowhvac.example</li>
    <li><svg class="ico"><use href="#i-web"/></svg>www.tallowhvac.example</li>
  </ul>
</section>

<!-- Invoice -->
<section class="page page--invoice" aria-label="Tax invoice">
  <div class="brand"><span class="brand__dot"></span><div><div class="brand__name">TALLOW</div><div class="brand__sub">HVAC SERVICES PTY LTD.</div></div></div>
  <h1 class="abs doc-title">TAX INVOICE</h1>
  <ul class="contact" style="left:27px;top:68px">
    <li><svg class="ico"><use href="#i-phone"/></svg>0400 123 456</li>
    <li><svg class="ico"><use href="#i-mail"/></svg>rod@tallowhvac.example</li>
    <li><svg class="ico"><use href="#i-web"/></svg>www.tallowhvac.example</li>
  </ul>
  <div class="abs meta" style="left:198px;top:58px">Invoice#</div>
  <div class="abs meta meta__value" style="right:28px;top:60px">52148</div>
  <div class="abs meta" style="left:198px;top:70px">Date</div>
  <div class="abs meta meta__value" style="right:28px;top:72px">01 / 02 / 2020</div>

  <table class="items">
    <thead><tr><th class="c-sl">SL.</th><th class="c-desc">Item Description</th><th class="c-price">Price</th><th class="c-qty">Qty.</th><th>Total</th></tr></thead>
    <tbody>
      <tr><td>1</td><td>Lorem Ipsum Dolor</td><td>$50.00</td><td>1</td><td>$50.00</td></tr>
      <tr><td>2</td><td>Pellentesque id neque ligula</td><td>$20.00</td><td>3</td><td>$60.00</td></tr>
      <tr><td>3</td><td>Interdum et malesuada fames</td><td>$10.00</td><td>2</td><td>$20.00</td></tr>
      <tr><td>4</td><td>Vivamus volutpat faucibus</td><td>$90.00</td><td>1</td><td>$90.00</td></tr>
      <tr class="blank"><td></td><td></td><td></td><td></td><td></td></tr>
    </tbody>
  </table>

  <div class="abs pay-note">By Electronic Funds<br>transfer (EFT)</div>
  <div class="abs sum" style="left:208px;top:285px">Sub Total:</div>
  <div class="abs sum" style="left:263px;top:285px">$220.00</div>
  <div class="abs sum" style="left:208px;top:296px">Tax:</div>
  <div class="abs sum" style="left:263px;top:296px">0.00%</div>
  <div class="sum-rule"></div>
  <div class="abs sum sum--total" style="left:208px;top:315px">Total:</div>
  <div class="abs sum sum--total sum--total-value" style="left:256px;top:315px">$220.00</div>

  <div class="abs due" style="left:27px;top:325px">Due Date</div>
  <div class="abs due" style="left:87px;top:325px">07-09-2023</div>
  <dl class="abs bank">
    <dt>Bank:</dt><dd>Harbour Bank</dd>
    <dt>Acc. Name:</dt><dd>Tallow HVAC Services</dd>
    <dt>BSB:</dt><dd>000 000</dd>
    <dt>Acc. No.</dt><dd>0000 0000 0000</dd>
  </dl>

  <ul class="signoff signoff--compact" style="top:396px;left:17px">
    <li class="signoff__name" style="padding-left:7px">ROD TALLOW</li>
    <li><svg class="ico"><use href="#i-phone"/></svg>0400 123 456</li>
    <li><svg class="ico"><use href="#i-mail"/></svg>rod@tallowhvac.example</li>
    <li><svg class="ico"><use href="#i-web"/></svg>www.tallowhvac.example</li>
    <li><svg class="ico"><use href="#i-pin"/></svg>PO Box 12 Eastvale, NSW 2000</li>
    <li><svg class="ico"><use href="#i-doc"/></svg>ABN: 10 203 405 607</li>
    <li><svg class="ico"><use href="#i-doc"/></svg>Licence No: 120450C</li>
    <li><svg class="ico"><use href="#i-doc"/></svg>ARC No: AU10203</li>
  </ul>
</section>

<!-- Quote -->
<section class="page page--quote" aria-label="Quote">
  <div class="brand"><span class="brand__dot"></span><div><div class="brand__name">TALLOW</div><div class="brand__sub">HVAC SERVICES PTY LTD.</div></div></div>
  <ul class="contact" style="left:14px;top:35px">
    <li><svg class="ico"><use href="#i-phone"/></svg>0400 123 456</li>
    <li><svg class="ico"><use href="#i-mail"/></svg>rod@tallowhvac.example</li>
    <li><svg class="ico"><use href="#i-web"/></svg>www.tallowhvac.example</li>
  </ul>
  <div class="abs fields">Name:<br><span class="plain">05/09/2023</span><br>Address:<br>Phone:<br>Email:</div>
  <div class="abs quote-ref">05 / 09 / 2023<br>QUOTE No: 1111</div>
  <div class="abs validity">VALID 30 DAYS</div>
  <div class="abs proposal">Air Conditioning &amp; Mechanical Ventilation Proposal for</div>
  <div class="proposal-line"></div>
  <p class="body-copy">Thank you for the opportunity to provide a quotation for the above-mentioned address. If you have any questions regarding the items listed below, please do not hesitate to contact me directly.</p>
  <div class="abs description">Description.</div>
  <div class="abs quote-total">Total $0,000.00 Including GST.</div>
  <div class="abs regards">Kind Regards,</div>
  <div class="signature" role="img" aria-label="Handwritten signature of Rod Tallow"></div>
  <ul class="signoff" style="top:408px">
    <li class="signoff__name" style="padding-left:8px">ROD TALLOW</li>
    <li><svg class="ico"><use href="#i-phone"/></svg>0400 123 456</li>
    <li><svg class="ico"><use href="#i-mail"/></svg>rod@tallowhvac.example</li>
    <li><svg class="ico"><use href="#i-web"/></svg>www.tallowhvac.example</li>
  </ul>
</section>
</body>
</html>
```